Need App for Impact Related Events

My app is to help with internal events. When you enter the prompted event code the next screen shows you everyone currently at the event. It will give you the ability to Start a conversation with someone you met at that event, or signal it is your turn to send a message. The next screen is a message thread with that person. I am looking for a design that incorporates the colors and ‘feel good’ emotion of our logo. I have pieced together a pretty good interpretation of what I’m looking for in the attached mockup by slicing and dicing designs. I also attached our logo mascot.Screens (see attached mockups)

Note 1: I do not like the picture on the screen used in screen one because it makes it seem like a dating app. I attached an alternative photo that can be used or present different ideas.

Note 2: On the login/signup screen (screen 2) I need an additional first and last name for login, you can try to fit this on one login screen or present a two step signup screen where that is presented in the second screen.

READ MOCKUP GUIDELINES UNDER Must Haves

Target Market(s)

People attending internal social impact events

Industry/Entity Type

Charity

Font styles to use
Sans Serif

Colors
86cfc6

Requirements
Must have
• Follow the screen mockups attached to project
• PLEASE READ
• I have provided a relatively close design of what I’m looking for in the mockups. Some screens need to be followed more closely to my design mockup than other. I have listed a guide below how how closely you should follow my mockup design exactly. Overall I would like to see some ideas of incorporating a few accent colors so it doesn’t appear SO Blue. I also attached some app inspiration designs I found from around the web
• Screen Mockup Guideline Follow %
• Screen 1: 65% - mostly on target, would like to see ways to make it not SO Blue and possibly creative places to add some explainer text describing the app
• Screen 2: 50% - general design idea is here, but more open
• Screen 3: 35% - a lot more room for design influence
• Screen 4: 70% - mostly on target, a little room for design influence/color scheme ideas
• Screen 5-6: 25% - a lot of room for design change/ideas/influence
• Screen 7-8: 80% - already very close to what I need, maybe open to slight sizing and color scheme ideas
• Screen 9: 15% - the most open for influence, only the general functionality of the screen is communicated here
Nice to have
• Please Read Mockup Guideline above. In large part I am looking for something to use some nice accent colors so it is not overwhelmingly blue and bring the whole design into a seamless style.
Should not have

```html
<!DOCTYPE html>
<html lang="en">
<head>
<meta charset="utf-8">
<title>KindHive – Onboarding Screens</title>
<link href="https://fonts.googleapis.com/css2?family=Nunito+Sans:wght@400;600;700&display=swap" rel="stylesheet">
<style>
  :root {
    --canvas: #efefef;
    --ink: #1d1d1d;
    --soft-ink: #3a3a3a;
    --muted: #8a8a8a;
    --teal: #1fbfc9;
    --teal-soft: #86cfc6;
    --mint: #3ee0b0;
    --navy-start: #2f86b8;
    --navy-end: #17578f;
    --violet: #a67ad0;
    --lilac: #8f80d6;
    --line: #e3e6e8;
    --white: #ffffff;
  }
  * { box-sizing: border-box; margin: 0; padding: 0; }
  html, body { width: 1200px; height: 1200px; overflow: hidden; }
  body {
    background: var(--canvas);
    font-family: "Nunito Sans", Arial, sans-serif;
    color: var(--ink);
    position: relative;
  }
  .brand-dot {
    position: absolute; left: 846px; top: 44px; width: 96px; height: 96px;
    border-radius: 50%; background: var(--teal-soft);
  }
  .hero-wordmark {
    position: absolute; left: 712px; top: 170px; width: 336px;
    font-size: 64px; font-weight: 700; color: var(--ink);
    text-align: center; line-height: 1.1;
  }
  .step-number {
    position: absolute; top: 386px; width: 232px; text-align: center;
    font-size: 22px; font-weight: 700;
  }
  .screen {
    position: absolute; top: 436px; width: 232px; height: 502px;
    background: var(--white); border-radius: 28px; overflow: hidden;
    box-shadow: 0 6px 22px rgba(0,0,0,0.06);
  }
  .status-bar {
    position: absolute; left: 0; top: 9px; width: 100%; padding: 0 20px;
    display: flex; justify-content: space-between; align-items: center;
    font-size: 10px; color: var(--muted); z-index: 2;
  }
  .status-bar.on-photo { color: var(--white); }
  .status-icons { display: flex; gap: 3px; align-items: center; }
  .back-arrow { position: absolute; left: 11px; top: 44px; }
  .home-indicator {
    position: absolute; left: 74px; top: 491px; width: 84px; height: 3px;
    border-radius: 2px; background: #bdbdbd;
  }
  .centered { position: absolute; left: 0; width: 100%; text-align: center; }
  .pill {
    position: absolute; left: 15px; width: 202px; height: 39px; border-radius: 20px;
    display: flex; align-items: center; justify-content: center;
    font-size: 12.5px; font-weight: 600; letter-spacing: 0.6px;
  }
  .pill-ghost {
    background: var(--white); color: var(--teal);
    box-shadow: 0 3px 12px rgba(0,0,0,0.07);
  }
  .pill-social {
    background: linear-gradient(90deg, var(--navy-start), var(--navy-end));
    color: var(--white);
  }
  .field {
    position: absolute; left: 15px; width: 202px; height: 24px;
    border-bottom: 1px solid var(--line);
    font-size: 9.5px; color: var(--muted); padding-left: 10px;
  }
  .field.is-active { border-bottom: 1px solid var(--teal); color: var(--ink); font-size: 11px; }
  .caret { display: inline-block; width: 1.5px; height: 15px; background: var(--teal); vertical-align: -3px; margin-left: 4px; }

  /* screen 1 */
  .welcome-photo {
    position: absolute; left: 0; top: 0; width: 232px; height: 300px;
    background: linear-gradient(160deg, var(--violet), var(--lilac) 60%, #7b7fd0);
  }
  .photo-wave { position: absolute; left: 0; top: 200px; }
  .carousel-dots { position: absolute; left: 22px; top: 248px; display: flex; gap: 6px; }
  .carousel-dots span { width: 5px; height: 5px; border-radius: 50%; background: var(--white); }
  .mascot-badge {
    position: absolute; left: 76px; top: 212px; width: 80px; height: 80px; border-radius: 50%;
    background: var(--white); box-shadow: 0 4px 14px rgba(0,0,0,0.08);
  }
  .badge-dot {
    position: absolute; border-radius: 50%; background: var(--teal-soft);
  }
  .app-name { top: 310px; font-size: 30px; font-weight: 700; color: var(--ink); }
  .pill-primary {
    left: 32px; width: 166px; height: 32px; top: 372px;
    background: linear-gradient(90deg, var(--mint), var(--teal));
    color: var(--white); font-size: 14px;
  }
  .login-link { top: 432px; font-size: 14px; font-weight: 700; letter-spacing: 1px; }
  .skyline {
    position: absolute; left: 0; top: 420px; width: 232px; height: 82px;
    background: linear-gradient(180deg, rgba(230,232,236,0) 0%, #eceef1 100%);
  }

  .small-copy { font-size: 9.5px; color: var(--soft-ink); line-height: 1.3; letter-spacing: 0.3px; }
  .link-copy { color: var(--teal); font-weight: 700; }
  .greeting { top: 84px; font-size: 12px; font-weight: 600; letter-spacing: 0.6px; }
  .guest-name { top: 102px; font-size: 15px; font-weight: 600; color: var(--teal); letter-spacing: 0.6px; }
  .section-title { top: 120px; font-size: 12px; font-weight: 600; letter-spacing: 0.8px; }
  .avatar-ring {
    position: absolute; left: 52px; top: 169px; width: 128px; height: 128px;
    border-radius: 50%; border: 2px solid #ececec;
    display: flex; align-items: center; justify-content: center;
  }
</style>
</head>
<body>

<div class="brand-dot"></div>
<div class="hero-wordmark">KindHive</div>

<div class="step-number" style="left:44px">1</div>
<div class="step-number" style="left:338px">2</div>
<div class="step-number" style="left:632px">3</div>
<div class="step-number" style="left:926px">4</div>

<!-- Screen 1: welcome -->
<section class="screen" style="left:44px">
  <div class="welcome-photo" role="img" aria-label="Photo of event guests chatting over coffee, under a violet tint"></div>
  <svg class="photo-wave" width="232" height="120" viewBox="0 0 232 120">
    <path d="M0 90 C60 95 110 70 150 40 C190 12 215 8 232 6 L232 120 L0 120 Z" fill="#ffffff"/>
  </svg>
  <div class="status-bar on-photo"><span>9:41</span>
    <span class="status-icons">
      <svg width="12" height="8"><rect x="0" y="5" width="2" height="3" fill="currentColor"/><rect x="3" y="3" width="2" height="5" fill="currentColor"/><rect x="6" y="1" width="2" height="7" fill="currentColor"/><rect x="9" y="0" width="2" height="8" fill="currentColor"/></svg>
      <svg width="16" height="8"><rect x="0.5" y="0.5" width="13" height="7" rx="1.5" fill="none" stroke="currentColor"/><rect x="2" y="2" width="10" height="4" fill="currentColor"/></svg>
    </span></div>
  <div class="carousel-dots"><span></span><span></span><span></span></div>
  <div class="mascot-badge">
    <div class="badge-dot" style="left:22px;top:22px;width:36px;height:36px"></div>
  </div>
  <div class="centered app-name">KindHive</div>
  <div class="pill pill-primary">CREATE ACCOUNT</div>
  <div class="skyline" role="img" aria-label="Faint city skyline illustration"></div>
  <div class="centered login-link">LOGIN</div>
</section>

<!-- Screen 2: sign up -->
<section class="screen" style="left:338px">
  <div class="status-bar"><span>9:41</span>
    <span class="status-icons">
      <svg width="12" height="8"><rect x="0" y="5" width="2" height="3" fill="currentColor"/><rect x="3" y="3" width="2" height="5" fill="currentColor"/><rect x="6" y="1" width="2" height="7" fill="currentColor"/><rect x="9" y="0" width="2" height="8" fill="currentColor"/></svg>
      <svg width="16" height="8"><rect x="0.5" y="0.5" width="13" height="7" rx="1.5" fill="none" stroke="currentColor"/><rect x="2" y="2" width="10" height="4" fill="currentColor"/></svg>
    </span></div>
  <svg class="back-arrow" width="10" height="14" viewBox="0 0 10 14"><path d="M8 1 L2 7 L8 13" fill="none" stroke="#1d1d1d" stroke-width="1.5"/></svg>
  <div class="pill pill-social" style="top:94px">START WITH LINKWAVE</div>
  <div class="centered small-copy" style="top:146px">Or, Sign up with email.</div>
  <div class="field is-active" style="top:194px">MAYA<span class="caret"></span></div>
  <div class="field" style="top:238px">Last Name</div>
  <div class="pill pill-ghost" style="top:287px">NEXT</div>
  <div class="centered small-copy" style="top:424px">By Signing up, You agree to our<br><span class="link-copy">Terms of Use</span> or <span class="link-copy">Privacy Policy</span>.</div>
  <div class="home-indicator"></div>
</section>

<!-- Screen 3: account details -->
<section class="screen" style="left:632px">
  <div class="status-bar"><span>9:41</span>
    <span class="status-icons">
      <svg width="12" height="8"><rect x="0" y="5" width="2" height="3" fill="currentColor"/><rect x="3" y="3" width="2" height="5" fill="currentColor"/><rect x="6" y="1" width="2" height="7" fill="currentColor"/><rect x="9" y="0" width="2" height="8" fill="currentColor"/></svg>
      <svg width="16" height="8"><rect x="0.5" y="0.5" width="13" height="7" rx="1.5" fill="none" stroke="currentColor"/><rect x="2" y="2" width="10" height="4" fill="currentColor"/></svg>
    </span></div>
  <svg class="back-arrow" width="10" height="14" viewBox="0 0 10 14"><path d="M8 1 L2 7 L8 13" fill="none" stroke="#1d1d1d" stroke-width="1.5"/></svg>
  <div class="centered greeting">WELCOME !</div>
  <div class="centered guest-name">MAYA LORNE</div>
  <div class="centered small-copy" style="top:140px">We need some more information<br>about you before to start</div>
  <div class="field" style="top:194px">Email</div>
  <div class="field" style="top:238px">Password (6+ Characters)</div>
  <div class="pill pill-ghost" style="top:287px">LET’S START</div>
  <div class="home-indicator"></div>
</section>

<!-- Screen 4: profile picture -->
<section class="screen" style="left:926px">
  <div class="status-bar"><span>9:41</span>
    <span class="status-icons">
      <svg width="12" height="8"><rect x="0" y="5" width="2" height="3" fill="currentColor"/><rect x="3" y="3" width="2" height="5" fill="currentColor"/><rect x="6" y="1" width="2" height="7" fill="currentColor"/><rect x="9" y="0" width="2" height="8" fill="currentColor"/></svg>
      <svg width="16" height="8"><rect x="0.5" y="0.5" width="13" height="7" rx="1.5" fill="none" stroke="currentColor"/><rect x="2" y="2" width="10" height="4" fill="currentColor"/></svg>
    </span></div>
  <div class="badge-dot" style="left:100px;top:70px;width:32px;height:32px"></div>
  <div class="centered section-title">ADD PROFILE PICTURE</div>
  <div class="avatar-ring">
    <svg width="42" height="46" viewBox="0 0 42 46" fill="none" stroke="#d8d8d8" stroke-width="1.6">
      <circle cx="21" cy="13" r="10"/>
      <path d="M3 44 C1 32 9 27 21 27 C33 27 41 32 39 44 Z"/>
    </svg>
  </div>
  <div class="centered small-copy" style="top:326px">Tap to select or edit picture</div>
  <div class="pill pill-ghost" style="top:359px">SET MY PICTURE</div>
  <div class="centered small-copy" style="top:455px">Skip Now</div>
  <div class="home-indicator"></div>
</section>

</body>
</html>
```